Security Warning Sign

We have an existing sign that needs an update. I have attached a picture of the current square sign. We need to maintain the same wording. It needs to be professional and appropriate to attach to our customers fence. Also attached is a copy of our building sign which may lend some inspiration and hopefully the ai format will assist. The final sign will be 600mm x 600mmOur website is www.harbourlinewatch.com.au

```html
<!DOCTYPE html>
<html lang="en">
<head>
<meta charset="utf-8">
<title>Security Warning Sign</title>
<link rel="stylesheet" href="https://fonts.googleapis.com/css2?family=Anton&family=Oswald:wght@700&family=Open+Sans:wght@800&display=swap">
<style>
  :root {
    --sign-black: #000000;
    --sign-orange: #f48724;
    --sign-white: #ffffff;
  }
  html, body {
    margin: 0;
    padding: 0;
    width: 1200px;
    height: 1200px;
    overflow: hidden;
    background: var(--sign-black);
  }
  .sign {
    position: relative;
    width: 1200px;
    height: 1200px;
    background: var(--sign-black);
  }
  .sign__header {
    position: absolute;
    left: 37px;
    top: 37px;
    width: 1126px;
    height: 451px;
    background: var(--sign-orange);
  }
  .sign__notice {
    position: absolute;
    left: 37px;
    top: 488px;
    width: 1126px;
    height: 472px;
    background: var(--sign-white);
  }
  .sign__art {
    position: absolute;
    inset: 0;
  }
  .headline {
    font-family: "Anton", Impact, sans-serif;
    fill: var(--sign-black);
  }
  .notice-line {
    font-family: "Oswald", "Arial Narrow", sans-serif;
    font-weight: 700;
    fill: var(--sign-black);
  }
  .company-name {
    font-family: "Open Sans", Arial, sans-serif;
    font-weight: 800;
    fill: var(--sign-white);
  }
  .company-dot {
    fill: var(--sign-orange);
  }
  .phone-icon__box {
    fill: var(--sign-orange);
  }
  .phone-icon__handset {
    fill: none;
    stroke: var(--sign-black);
    stroke-width: 3;
    stroke-linecap: round;
  }
  .phone-number {
    font-family: "Oswald", "Arial Narrow", sans-serif;
    font-weight: 700;
    fill: var(--sign-white);
  }
</style>
</head>
<body>
<main class="sign">
  <div class="sign__header"></div>
  <div class="sign__notice"></div>

  <svg class="sign__art" width="1200" height="1200" viewBox="0 0 1200 1200" xmlns="http://www.w3.org/2000/svg">
    <text class="headline" x="96" y="350" font-size="262" textLength="1011" lengthAdjust="spacingAndGlyphs">WARNING!</text>

    <text class="notice-line" x="59" y="604" font-size="92" textLength="1084" lengthAdjust="spacingAndGlyphs">ELECTRONIC SURVEILLANCE</text>
    <text class="notice-line" x="83" y="721" font-size="92" textLength="1006" lengthAdjust="spacingAndGlyphs">AND RECORDING DEVICES</text>
    <text class="notice-line" x="124" y="837" font-size="92" textLength="954" lengthAdjust="spacingAndGlyphs">INSTALLED IN THIS AREA</text>

    <circle class="company-dot" cx="135" cy="1066" r="58"/>
    <text class="company-name" x="236" y="1042" font-size="40" textLength="248" lengthAdjust="spacingAndGlyphs">HARBOURLINE</text>
    <text class="company-name" x="236" y="1083" font-size="40" textLength="160" lengthAdjust="spacingAndGlyphs">WATCH</text>
    <text class="company-name" x="236" y="1124" font-size="40" textLength="206" lengthAdjust="spacingAndGlyphs">SERVICES</text>

    <g class="phone-icon">
      <rect class="phone-icon__box" x="682" y="1053" width="51" height="53" rx="6"/>
      <path class="phone-icon__handset" d="M702 1064 q-8 14 4 32 M702 1064 l4 -2 M706 1096 l4 -2 M711 1061 l0 6 M713 1095 l4 5"/>
    </g>
    <text class="phone-number" x="745" y="1106" font-size="68" textLength="398" lengthAdjust="spacingAndGlyphs">1300 555 014</text>
  </svg>
</main>
</body>
</html>
```